Logo and Business Card for Dental Office

We are opening a periodontal office (dental specialist for dental implants and gum diseases). It is a brand new state of the art facility with a focus on the most effective treatments for retaining natural teeth, or replacing teeth with implants when they must be lost. Strong emphasis on customer service and amenities for patient comfort. We are located just outside of Boston, MA.

Target Market(s)

potential adult patients, dentists in the community that will refer patients for specialized care

Industry/Entity Type

Dental

Requirements
Must have
• business name, address, phone number, website
Marcus T. Pellinger, DMD LLC
427 Corliss Street, Ste 305
Larkton, ST 01694
555-201-0172
555-201-0148 Fax
DrPellinger.example

the uploaded file has a rough version of what I'm looking for in the logo, I like the colors but it can be varies some.
Nice to have
• simple logo or symbol on business card, one possible idea I had was an abstract symbol of a screw or threads that might represent a dental implant, the attached file gives an idea of where to start.
Should not have
• I want a professional feel, no cartoons of teeth that appear childish, etc
The font should be easy to read with no curly/swirly shapes.

```html
<!DOCTYPE html>
<html lang="en">
<head>
<meta charset="utf-8">
<title>Marcus T. Pellinger, DMD LLC – Business Card</title>
<link rel="stylesheet" href="https://fonts.googleapis.com/css2?family=Barlow:wght@400;500&family=Quicksand:wght@700&display=swap">
<style>
  :root {
    --brand-red: #9b0a02;
    --panel-grey: #e6e6e6;
    --ink: #2f2f2f;
    --page: #ffffff;
  }
  html, body {
    margin: 0;
    padding: 0;
    width: 1200px;
    height: 927px;
    overflow: hidden;
    background: var(--page);
  }
  .canvas {
    position: relative;
    width: 1200px;
    height: 927px;
  }
  .card {
    position: absolute;
    left: 83px;
    top: 162px;
    width: 998px;
    height: 576px;
    background: var(--brand-red);
  }
  .card__panel {
    position: absolute;
    left: 12px;
    top: 145px;
    width: 974px;
    height: 419px;
    background: var(--panel-grey);
  }
  .card__title {
    position: absolute;
    left: 40px;
    top: 84px;
    width: 920px;
    height: 70px;
    overflow: visible;
  }
  .card__title text {
    font-family: "Quicksand", sans-serif;
    font-weight: 700;
    font-size: 64px;
    fill: var(--panel-grey);
  }
  .specialty {
    position: absolute;
    left: 39px;
    top: 161px;
    margin: 0;
    font-family: "Barlow", sans-serif;
    font-weight: 400;
    font-size: 44px;
    line-height: 1;
    letter-spacing: 1.2px;
    color: var(--brand-red);
    white-space: nowrap;
  }
  .contact {
    position: absolute;
    left: 39px;
    top: 204px;
    margin: 0;
    font-family: "Barlow", sans-serif;
    font-weight: 500;
    font-size: 40px;
    line-height: 59px;
    color: var(--ink);
    font-style: normal;
    white-space: nowrap;
  }
  .website {
    position: absolute;
    right: 205px;
    top: 490px;
    margin: 0;
    font-family: "Quicksand", sans-serif;
    font-weight: 700;
    font-size: 46px;
    line-height: 1;
    color: var(--brand-red);
    text-transform: uppercase;
    white-space: nowrap;
  }
  .brand-mark {
    position: absolute;
    left: 770px;
    top: 200px;
    width: 210px;
    display: flex;
    flex-direction: column;
    align-items: center;
    gap: 18px;
  }
  .brand-mark__dot {
    width: 140px;
    height: 140px;
    border-radius: 50%;
    background: var(--brand-red);
  }
  .brand-mark__name {
    font-family: "Barlow", sans-serif;
    font-weight: 500;
    font-size: 40px;
    line-height: 1;
    color: var(--brand-red);
  }
</style>
</head>
<body>
  <main class="canvas">
    <section class="card">
      <div class="card__panel"></div>
      <svg class="card__title" viewBox="0 0 920 70" aria-label="Marcus T. Pellinger, DMD LLC">
        <text x="0" y="58" textLength="915" lengthAdjust="spacingAndGlyphs">MARCUS T. PELLINGER, DMD LLC</text>
      </svg>
      <p class="specialty">PERIODONTICS &amp; DENTAL IMPLANTS</p>
      <address class="contact">
        427 Corliss Street, Ste 305<br>
        Larkton, ST 01694<br>
        Ph:&nbsp; 555-201-0172<br>
        Fax: 555-201-0148
      </address>
      <p class="website">DrPellinger.example</p>
      <div class="brand-mark">
        <span class="brand-mark__dot"></span>
        <span class="brand-mark__name">Pellinger</span>
      </div>
    </section>
  </main>
</body>
</html>
```